Stonebay Towing Business Card

Towing
Accident towing
Mechanical breakdown
Insurance, salvage and recovery
4wd off road towing
Light & Heavy towing
8347 2516
24 hour business 7 days

Logo can be whole size on front

Industry/Entity Type

Towing/ transport

Contact Information for Business Card

The above

```html
<!DOCTYPE html>
<html lang="en">
<head>
<meta charset="utf-8">
<title>Stonebay Towing Business Card</title>
<link href="https://fonts.googleapis.com/css2?family=Arimo:wght@400;700&display=swap" rel="stylesheet">
<style>
  :root {
    --backdrop: #3d3d3d;
    --brand-red: #d21f26;
    --card-white: #ffffff;
    --ink-dark: #2b2b2b;
    --ink-grey: #8a8a8a;
    --rule-grey: #d4d4d4;
  }
  * { box-sizing: border-box; margin: 0; padding: 0; }
  html, body {
    width: 1200px; height: 803px; overflow: hidden;
    background: var(--backdrop);
    font-family: "Arimo", Arial, sans-serif;
  }
  .sheet {
    width: 1200px; height: 803px;
    display: flex; align-items: center; justify-content: center; gap: 40px;
  }
  .card {
    width: 540px; height: 310px;
    border-radius: 22px;
    position: relative;
    overflow: hidden;
    box-shadow: 0 14px 30px rgba(0,0,0,.35);
  }

  /* Contact side */
  .card--contact { background: var(--card-white); }
  .brand-mark {
    position: absolute; left: 40px; top: 50%;
    transform: translateY(-50%);
    width: 200px;
    display: flex; align-items: center; gap: 12px;
  }
  .brand-mark__dot {
    width: 16px; height: 16px; border-radius: 50%;
    background: var(--brand-red); flex: none;
  }
  .brand-mark__name {
    color: var(--brand-red); font-weight: 700; font-size: 30px;
    line-height: 1.05;
  }
  .divider {
    position: absolute; left: 262px; top: 40px;
    width: 1px; height: 140px;
    background: linear-gradient(var(--card-white), var(--rule-grey) 30%, var(--rule-grey) 70%, var(--card-white));
  }
  .person { position: absolute; left: 288px; top: 52px; right: 20px; }
  .person__name {
    color: var(--brand-red); font-weight: 700; font-size: 22px;
    letter-spacing: .3px;
  }
  .person__role { color: var(--ink-grey); font-size: 13px; margin-top: 3px; }
  .contacts { list-style: none; margin-top: 18px; }
  .contacts li {
    display: flex; align-items: center; gap: 9px;
    color: var(--ink-dark); font-size: 13.5px; line-height: 21px;
    white-space: nowrap;
  }
  .contacts svg { width: 12px; height: 12px; fill: var(--brand-red); flex: none; }
  .hours {
    position: absolute; left: 288px; bottom: 44px;
    display: flex; align-items: center; gap: 10px;
    color: var(--ink-dark); font-size: 14px;
  }
  .hours svg { width: 30px; height: 30px; }

  /* Services side */
  .card--services { background: var(--brand-red); }
  .hero-name {
    position: absolute; left: 0; right: 0; top: 92px;
    text-align: center;
    color: var(--card-white); font-weight: 700; font-size: 54px; line-height: 1;
  }
  .services {
    position: absolute; left: 10px; right: 10px; bottom: 46px;
    text-align: center; color: var(--card-white); font-size: 14px; line-height: 24px;
    white-space: nowrap;
  }
  .services span + span::before {
    content: "\2022"; margin: 0 8px;
  }
</style>
</head>
<body>
<main class="sheet">

  <section class="card card--contact">
    <div class="brand-mark">
      <span class="brand-mark__dot"></span>
      <span class="brand-mark__name">Stonebay<br>Towing</span>
    </div>
    <div class="divider"></div>

    <div class="person">
      <h1 class="person__name">DANIEL HART</h1>
      <p class="person__role">President</p>
      <ul class="contacts">
        <li>
          <svg viewBox="0 0 24 24"><path d="M6.6 10.8a15.1 15.1 0 0 0 6.6 6.6l2.2-2.2a1 1 0 0 1 1-.25 11.4 11.4 0 0 0 3.6.57 1 1 0 0 1 1 1V20a1 1 0 0 1-1 1A17 17 0 0 1 3 4a1 1 0 0 1 1-1h3.5a1 1 0 0 1 1 1c0 1.25.2 2.45.57 3.57a1 1 0 0 1-.25 1z"/></svg>
          8347 2516
        </li>
        <li>
          <svg viewBox="0 0 24 24"><path d="M2 5h20v14H2z M2 5l10 8 10-8" fill="none" stroke="#d21f26" stroke-width="2.4"/></svg>
          info@stonebaytowing.com
        </li>
        <li>
          <svg viewBox="0 0 24 24"><circle cx="12" cy="12" r="10"/></svg>
          www.stonebaytowing.com
        </li>
      </ul>
    </div>

    <div class="hours">
      <svg viewBox="0 0 32 32">
        <path d="M27 12A12 12 0 1 0 28 18" fill="none" stroke="#d21f26" stroke-width="2"/>
        <path d="M24 9l4 3 1-5z" fill="#d21f26"/>
        <text x="16" y="19.5" text-anchor="middle" font-family="Arimo, Arial, sans-serif" font-size="8" font-weight="700" fill="#d21f26">24/7</text>
      </svg>
      24 hour business 7 days
    </div>
  </section>

  <section class="card card--services">
    <p class="hero-name">Stonebay Towing</p>
    <p class="services">
      <span>Towing</span><span>Accident towing</span><span>Mechanical breakdown</span><br>
      <span>Insurance, salvage &amp; recovery</span><span>4wd off road towing</span><span>Light &amp; Heavy towing</span>
    </p>
  </section>

</main>
</body>
</html>
```